WebDesign Flyer - A5 Double Sided

We create a complete web presence for local businesses.
A comprehensive background on our services and company can be found at www.keenpixelhouse.co.uk and on the attached sales document.

We want these flyers (a5, double sided, colour) to portray us as a local, professional and friendly service that will take care fully of a business's online presence. This includes website, hosting, email, domain AND IMPORTANTLY: we also can build them a business profile on business directory websites such as NookFinder, StreetBrowse, Marbel Spots, Zorb etc. which helps them increase their profit.

Target Market(s)

Small to medium businesses found on the high street. eg: restaurants, physios, doctors, retail shops, salons, hairdressers, as well as more corporate businesses like accountancy firms and lawyers.

Industry/Entity Type

Business Directory

Requirements
Must have
• Full project files provided with all required elements if design is chosen. Design to mention: sites can be updated in less than 1 minute in 3 clicks, No contracts, money back guarantee (no risk), prices from £400, SEO as standard, keenpixelhouse.co.uk, 020 7946 0318, info@keenpixelhouse.co.uk, 10% discount with this flyer until December 20th 2010.
Nice to have
• To mention: dedicated support, business photos (see keenpixelhouse.co.uk/features), Chatterly, Quippo, ReelBox, Snapry, WorkNest Integration, free consultation, logos of services we provide (see logos.zip for examples).
Should not have
• our logo featured too prominently.

```html
<!DOCTYPE html>
<html lang="en">
<head>
<meta charset="utf-8">
<title>Keen Pixel House – A5 Flyer</title>
<link rel="stylesheet" href="https://fonts.googleapis.com/css2?family=Alfa+Slab+One&display=swap">
<style>
  :root {
    --sky: #55bdf5;
    --sky-light: #bfe7fb;
    --sky-pale: #e6f6fe;
    --navy: #1d5fa8;
    --ink: #1a56a3;
    --lime: #e3ff24;
    --lime-edge: #b8cf00;
    --white: #ffffff;
    --page: #ffffff;
  }
  * { box-sizing: border-box; margin: 0; padding: 0; }
  html, body { width: 1200px; height: 1070px; overflow: hidden; background: var(--page); }
  body { font-family: "Alfa Slab One", serif; position: relative; }

  .flyer {
    position: absolute;
    overflow: hidden;
    box-shadow: 4px 4px 8px rgba(0,0,0,0.45);
    border: 1px solid #d6d6d6;
  }
  .flyer-front { left: 50px; top: 44px; width: 534px; height: 752px; background: var(--white); }
  .flyer-back  { left: 614px; top: 157px; width: 538px; height: 756px;
    background: linear-gradient(180deg, var(--sky) 0%, #8fd3f8 40%, var(--sky-pale) 68%, var(--white) 100%); }

  .backdrop { position: absolute; inset: 0; }

  .brand {
    position: absolute;
    display: flex;
    align-items: center;
    gap: 8px;
    color: var(--sky);
    white-space: nowrap;
  }
  .brand-dot { border-radius: 50%; background: var(--lime); flex: none; }
  .brand-name { line-height: 1; }

  .headline {
    position: absolute;
    color: var(--white);
    white-space: nowrap;
    text-shadow: -1px -1px 0 var(--navy), 1px -1px 0 var(--navy), -1px 1px 0 var(--navy),
                 1px 1px 0 var(--navy), 3px 3px 0 var(--navy);
    transform: translateX(-50%);
    line-height: 1;
  }
  .plus {
    position: absolute;
    color: var(--lime);
    font-size: 46px;
    line-height: 1;
    transform: translateX(-50%);
    text-shadow: -2px -2px 0 var(--white), 2px -2px 0 var(--white), -2px 2px 0 var(--white), 2px 2px 0 var(--white);
  }
  .equals {
    position: absolute;
    left: 158px; top: 338px;
    width: 50px;
  }
  .equals span {
    display: block; height: 11px; margin-bottom: 8px;
    background: var(--lime); border: 2px solid var(--white);
  }
  .badge-ring { position: absolute; left: 50px; top: 291px; }

  .closing {
    position: absolute;
    color: var(--lime);
    white-space: nowrap;
    line-height: 1;
    text-shadow: -1px -1px 0 var(--navy), 1px -1px 0 var(--navy), -1px 1px 0 var(--navy),
                 1px 1px 0 var(--navy), 3px 3px 0 var(--navy);
  }

  .perk {
    position: absolute;
    color: var(--white);
    font-size: 21px;
    white-space: nowrap;
    line-height: 1;
    text-shadow: 1px 1px 0 var(--navy), 2px 2px 0 var(--navy);
  }
  .bullet {
    position: absolute;
    border-radius: 50%;
    background: radial-gradient(circle at 40% 35%, #f6ff9a, var(--lime) 60%, var(--lime-edge));
    border: 1px solid var(--lime-edge);
  }
  .pounds {
    position: absolute;
    color: var(--white);
    letter-spacing: -1px;
    line-height: 1;
    text-shadow: 1px 1px 0 var(--navy), 2px 2px 0 var(--navy);
  }
  .icon { position: absolute; }

  .offer-rings { position: absolute; left: 67px; top: 461px; }
  .offer {
    position: absolute;
    left: 151px; top: 543px;
    transform: translate(-50%, -50%) rotate(-20deg);
    text-align: center;
    color: var(--ink);
    line-height: 1.05;
    white-space: nowrap;
  }
  .offer-value { font-size: 33px; display: block; }
  .offer-terms { font-size: 18px; display: block; }

  .contact {
    position: absolute;
    left: 28px;
    font-size: 14px;
    white-space: nowrap;
  }
  .contact-phone { top: 668px; color: var(--ink); }
  .contact-email { top: 697px; color: var(--sky); }
</style>
</head>
<body>

  <section class="flyer flyer-front">
    <svg class="backdrop" width="534" height="752" viewBox="0 0 534 752">
      <path d="M0,62 C120,40 250,58 335,130 C400,185 460,212 534,222 V752 H0 Z" fill="#55bdf5"/>
      <path d="M0,110 C140,95 260,120 340,170 C410,215 470,238 534,244" fill="none" stroke="#ffffff" stroke-width="14" opacity="0.9"/>
      <path d="M0,128 C140,115 260,140 340,190 C410,235 470,258 534,262" fill="none" stroke="#bfe7fb" stroke-width="4"/>
      <rect x="80" y="110" width="180" height="90" rx="40" fill="#8fd3f8" opacity="0.5" role="img" aria-label="Soft floral flourish"/>
      <circle cx="286" cy="196" r="10" fill="none" stroke="#bfe7fb" stroke-width="2"/>
      <circle cx="302" cy="178" r="5" fill="none" stroke="#bfe7fb" stroke-width="2"/>
      <circle cx="450" cy="298" r="18" fill="none" stroke="#bfe7fb" stroke-width="2"/>
      <circle cx="478" cy="330" r="8" fill="none" stroke="#bfe7fb" stroke-width="2"/>
      <path d="M0,578 C150,598 300,618 534,660" fill="none" stroke="#ffffff" stroke-width="10"/>
      <path d="M0,590 C150,610 300,630 534,672 V752 H0 Z" fill="#e3ff24"/>
    </svg>

    <div class="brand" style="left:262px; top:30px;">
      <span class="brand-dot" style="width:26px; height:26px;"></span>
      <span class="brand-name" style="font-size:18px;">KEEN PIXEL HOUSE</span>
    </div>

    <svg class="badge-ring" width="120" height="120" viewBox="0 0 120 120">
      <circle cx="60" cy="60" r="56" fill="none" stroke="#ffffff" stroke-width="3"/>
      <circle cx="60" cy="60" r="48" fill="#ffffff"/>
    </svg>
    <div class="equals"><span></span><span></span></div>

    <div class="headline" style="left:324px; top:233px; font-size:30px;">BESPOKE WEBSITE</div>
    <div class="plus" style="left:329px; top:281px;">+</div>
    <div class="headline" style="left:330px; top:336px; font-size:37px;">S.E.O</div>
    <div class="plus" style="left:329px; top:389px;">+</div>
    <div class="headline" style="left:307px; top:452px; font-size:33px;">BUSINESS LISTINGS</div>
    <div class="plus" style="left:329px; top:500px;">+</div>
    <div class="headline" style="left:330px; top:560px; font-size:32px;">SOCIAL MEDIA</div>

    <div class="closing" style="left:65px; top:630px; font-size:40px;">and</div>
    <div class="closing" style="left:33px; top:680px; font-size:41px;">LOTS MORE!</div>
  </section>

  <section class="flyer flyer-back">
    <svg class="backdrop" width="538" height="756" viewBox="0 0 538 756">
      <rect x="20" y="20" width="220" height="140" rx="60" fill="#ffffff" opacity="0.12" role="img" aria-label="Faint floral flourish"/>
      <path d="M0,420 C90,330 200,300 300,360 C380,410 450,400 538,330" fill="none" stroke="#ffffff" stroke-width="16" opacity="0.85"/>
      <path d="M0,445 C90,355 200,325 300,385 C380,435 450,425 538,355" fill="none" stroke="#8fd3f8" stroke-width="3"/>
      <rect x="260" y="330" width="260" height="200" rx="90" fill="#8fd3f8" opacity="0.35" role="img" aria-label="Floral vine flourish"/>
      <circle cx="478" cy="260" r="15" fill="none" stroke="#ffffff" stroke-width="2"/>
      <circle cx="400" cy="230" r="4" fill="none" stroke="#ffffff" stroke-width="2"/>
      <circle cx="384" cy="372" r="5" fill="none" stroke="#ffffff" stroke-width="2"/>
      <circle cx="506" cy="560" r="14" fill="none" stroke="#8fd3f8" stroke-width="2"/>
    </svg>

    <span class="bullet" style="left:66px; top:28px; width:22px; height:22px;"></span>
    <div class="perk" style="left:96px; top:28px;">Sites updated -</div>
    <div class="perk" style="left:155px; top:58px;">in LESS THAN A MINUTE</div>
    <svg class="icon" style="left:283px; top:8px;" width="42" height="42" viewBox="0 0 40 40" role="img" aria-label="Clock">
      <circle cx="20" cy="20" r="17" fill="#ffffff" stroke="#1d5fa8" stroke-width="3"/>
      <path d="M20,10 V20 L27,25" fill="none" stroke="#1d5fa8" stroke-width="3" stroke-linecap="round"/>
    </svg>

    <span class="bullet" style="left:116px; top:93px; width:26px; height:26px;"></span>
    <div class="perk" style="left:155px; top:96px;">NO contracts</div>
    <svg class="icon" style="left:313px; top:88px;" width="40" height="40" viewBox="0 0 38 38" role="img" aria-label="Torn contract">
      <circle cx="19" cy="19" r="17" fill="#ffffff" stroke="#1d5fa8" stroke-width="2"/>
      <rect x="10" y="10" width="16" height="19" fill="#ffffff" stroke="#1d5fa8" stroke-width="2" transform="rotate(-15 18 19)"/>
      <path d="M12,16 H24 M12,20 H24 M12,24 H20" stroke="#1d5fa8" stroke-width="1.5" transform="rotate(-15 18 19)"/>
    </svg>

    <div class="pounds" style="left:58px; top:142px; font-size:28px;">£££</div>
    <span class="bullet" style="left:163px; top:144px; width:28px; height:28px;"></span>
    <div class="perk" style="left:203px; top:147px;">Money back GUARANTEE</div>

    <span class="bullet" style="left:35px; top:202px; width:14px; height:14px;"></span>
    <div class="perk" style="left:59px; top:198px;">From £400 ONLY</div>
    <div class="pounds" style="left:285px; top:196px; font-size:22px;">£££</div>

    <span class="bullet" style="left:80px; top:239px; width:28px; height:28px;"></span>
    <div class="perk" style="left:118px; top:243px;">Promotion via Chatterly,</div>
    <div class="perk" style="left:215px; top:276px;">Snapry, Quippo &amp;</div>
    <div class="perk" style="left:340px; top:308px;">ReelBox etc.</div>

    <svg class="offer-rings" width="168" height="168" viewBox="0 0 168 168">
      <circle cx="84" cy="82" r="78" fill="none" stroke="#e3ff24" stroke-width="4"/>
      <circle cx="84" cy="82" r="70" fill="none" stroke="#e3ff24" stroke-width="2"/>
      <circle cx="84" cy="82" r="63" fill="#e3ff24" opacity="0.25"/>
    </svg>
    <div class="offer">
      <span class="offer-value">10% OFF</span>
      <span class="offer-terms">with this flyer</span>
      <span class="offer-terms">(until 20.12.2010)</span>
    </div>

    <div class="contact contact-phone">020 7946 0318</div>
    <div class="contact contact-email">info@keenpixelhouse.co.uk</div>

    <div class="brand" style="left:300px; top:678px;">
      <span class="brand-dot" style="width:24px; height:24px;"></span>
      <span class="brand-name" style="font-size:15px;">KEEN PIXEL HOUSE</span>
    </div>
  </section>

  <div class="brand" style="left:44px; top:982px;">
    <span class="brand-dot" style="width:40px; height:40px;"></span>
    <span class="brand-name" style="font-size:27px;">KEEN PIXEL HOUSE</span>
  </div>

</body>
</html>
```